Heritage Hollow Business Cards

Require a business card design. <br/><br/>Needs to include logo (either round or long version) plus these details:<br/>Maya Torvel<br/>Heritage Hollow<br/>maya@quonbrook.com.au<br/>02 6481 7390<br/>PO Box Glenwarra NSW 2913<br/>www.heritagehollow.com.au<br/><br/>I need in an editable format so that I can create for multiple staff members. <br/><br/>

Target Market(s)

We are an online store selling renovation products to home owners are builders. Looking for a classic classy design.

Industry/Entity Type

Home And Garden

Contact Information for Business Card

Maya Torvel
Heritage Hollow
maya@quonbrook.com.au
02 6481 7390
PO Box Glenwarra NSW 2913
www.heritagehollow.com.au

Colors

Designer to choose colors to be used in the design.

Requirements
Must have
• Must include Logo.

```html
<!DOCTYPE html>
<html lang="en">
<head>
<meta charset="utf-8">
<title>Heritage Hollow Business Cards</title>
<link href="https://fonts.googleapis.com/css2?family=Lato:wght@400;900&display=swap" rel="stylesheet">
<style>
  :root {
    --ink: #0a0a0a;
    --paper: #ffffff;
    --stage: #d9d9d9;
    --mid-grey: #6f6f6f;
    --soft-grey: #8a8a8a;
    --line-grey: #8f8f8f;
  }
  * { box-sizing: border-box; margin: 0; padding: 0; }
  html, body {
    width: 1200px; height: 900px; overflow: hidden;
    background: var(--stage);
    font-family: "Lato", sans-serif;
  }
  .card {
    position: absolute;
    left: 240px;
    width: 720px;
    height: 410px;
    border-radius: 26px;
    overflow: hidden;
    box-shadow: 0 8px 24px rgba(0,0,0,0.25);
  }
  /* Back side */
  .card-back {
    top: 30px;
    background: var(--ink);
    display: flex;
    align-items: center;
    justify-content: center;
    gap: 20px;
  }
  .brand-dot {
    width: 64px; height: 64px;
    border: 2px solid var(--paper);
    border-radius: 50%;
  }
  .brand-name-back {
    color: var(--paper);
    font-weight: 400;
    font-size: 56px;
    letter-spacing: 0.5px;
  }
  /* Front side */
  .card-front {
    top: 465px;
    background: var(--paper);
  }
  .front-shape { position: absolute; inset: 0; }
  .holder {
    position: absolute; left: 44px; top: 100px;
  }
  .holder-name {
    font-weight: 900; font-size: 34px; color: var(--ink);
  }
  .holder-company {
    font-weight: 400; font-size: 20px; color: var(--mid-grey); margin-top: 2px;
  }
  .brand-badge {
    position: absolute; right: 40px; top: 18px;
    width: 180px; height: 180px;
    border: 1.5px solid var(--soft-grey);
    border-radius: 50%;
    display: flex; align-items: center; justify-content: center;
    text-align: center;
    font-weight: 400; font-size: 27px; line-height: 1.1;
    color: var(--ink);
  }
  .contact {
    position: absolute; left: 64px; top: 272px;
    color: var(--paper);
    font-size: 16px; line-height: 20px;
  }
  .address { margin-bottom: 6px; }
  .contact-row {
    display: flex; align-items: center; gap: 12px;
    height: 24px;
  }
  .contact-row svg { width: 17px; height: 17px; flex: none; }
</style>
</head>
<body>
  <section class="card card-back">
    <span class="brand-dot"></span>
    <span class="brand-name-back">Heritage Hollow</span>
  </section>

  <section class="card card-front">
    <svg class="front-shape" viewBox="0 0 720 410" preserveAspectRatio="none">
      <path class="wave-band" d="M0 410 V300 C40 240 150 215 300 208 C420 202 520 206 600 206 C660 206 690 200 720 194 V410 Z" fill="var(--ink)"/>
      <path class="wave-accent" d="M0 278 C40 215 150 190 300 186 C370 184 420 184 470 186 C420 191 370 193 300 196 C155 202 45 232 0 292 Z" fill="var(--line-grey)"/>
    </svg>

    <div class="holder">
      <div class="holder-name">Maya Torvel</div>
      <div class="holder-company">Heritage Hollow</div>
    </div>

    <div class="brand-badge">Heritage<br>Hollow</div>

    <div class="contact">
      <div class="address">PO Box Glenwarra<br>NSW 2913</div>
      <div class="contact-row">
        <svg viewBox="0 0 24 24" fill="var(--paper)"><path d="M6.6 10.8a15 15 0 0 0 6.6 6.6l2.2-2.2a1 1 0 0 1 1-.25 11 11 0 0 0 3.6.6 1 1 0 0 1 1 1V20a1 1 0 0 1-1 1A17 17 0 0 1 3 4a1 1 0 0 1 1-1h3.5a1 1 0 0 1 1 1 11 11 0 0 0 .6 3.6 1 1 0 0 1-.25 1z"/></svg>
        <span>02 6481 7390</span>
      </div>
      <div class="contact-row">
        <svg viewBox="0 0 24 24" fill="none" stroke="var(--paper)" stroke-width="2"><rect x="3" y="5" width="18" height="14"/><path d="M3 5l9 8 9-8"/></svg>
        <span>maya@quonbrook.com.au</span>
      </div>
      <div class="contact-row">
        <svg viewBox="0 0 24 24" fill="none" stroke="var(--paper)" stroke-width="1.8"><circle cx="12" cy="12" r="9"/><path d="M3 12h18M12 3c3 3 3 15 0 18M12 3c-3 3-3 15 0 18"/></svg>
        <span>www.heritagehollow.com.au</span>
      </div>
    </div>
  </section>
</body>
</html>
```